Background of Our Business: TQB Financial Services provides accounting and tax services to small businesses. Website: www.tqbfsx.com.au. Our slogan is: one stop finance department service for small businesses.
I would like a flyer design with 2 sides.
1st side)
Business Logo; TQB - Finance Department Service for Small Businesses (Please refer file 1 as attached)

Large text of: Too many things going on? Smaller text: Let us reduce your input into accounts, you can focus on more value adding areas.

Our Services: Bookkeeping, Payroll, Financial Statement, Tax Advisory, Tax Return, Business Performance Measurement, Business Decision Support, Assistance in Loan Applications, and much more.

Why Us: Our clients are handpicked, we are fully committed to your business, and our works are performed at corporate standard. We utilise technology to save your accounting cost, monitor your compliance risks, provide solid data for business decision making, and be your representative in dealing with banks and NRB. (Please also refer file 2 as attached)

Contact details: Address: 58 Dunmore Street, Brindale, WA 6107
PO Box 2493, West Harlow, WA 6983
Tel: (08) 6287 3914; Mob: 0491 738 226

2nd side)
Our Pricing: Charge by transaction volumes; Fixed fee advised beforehand. hourly rate please refer file 4 as attached.

Our 'Gold' level service subscriber receives:
Frequent bookkeeping, payroll, and financial reporting services
Integrate tax advisory, compliance risk monitoring and control
Free regular preliminary business performance check
Free assistance in commercial loan and mortgage application
Free hand picked business insights for your industry
Free representative service for you in dealing with banks, NRB.

Coupon Section: Sign up now and receive 10% off for your next 12 months bill. Valid until 31/07/2016.

```html
<!DOCTYPE html>
<html lang="en">
<head>
<meta charset="utf-8">
<title>TQB Financial Services – Flyer</title>
<link rel="stylesheet" href="https://fonts.googleapis.com/css2?family=Gelasio:wght@400;700&family=PT+Sans:wght@400;700&family=Ubuntu:wght@500;700&display=swap">
<style>
  :root{
    --navy:#17499a;
    --cyan:#13aecd;
    --brown:#5b3d20;
    --ink:#1b1b1b;
    --link-blue:#1d5aa6;
    --paper-top:#ffffff;
    --paper-bottom:#e3e4e6;
    --stage:#63686c;
    --gold-grey:#7d7d7d;
    --ribbon:#f0a23a;
  }
  *{box-sizing:border-box;margin:0;padding:0}
  html,body{width:1200px;height:1200px;overflow:hidden;background:var(--stage)}
  .canvas{position:relative;width:1200px;height:1200px;overflow:hidden;background:var(--stage)}

  .flyer{position:absolute;width:664px;height:939px;overflow:hidden;transform:scale(.8);transform-origin:0 0;
    background:linear-gradient(160deg,var(--paper-top) 0%,#f2f3f4 45%,var(--paper-bottom) 100%);
    font-family:"PT Sans",sans-serif;color:var(--ink)}
  .flyer--services{left:50.4px;top:22.4px}
  .flyer--pricing{left:612.8px;top:398.4px}
  .flyer__shapes{position:absolute;left:0;top:0;width:664px;height:939px}
  .abs{position:absolute}

  .slogan{font-family:"Gelasio",serif;font-weight:700;font-size:21px;color:#fff;white-space:nowrap;line-height:1}
  .brand{position:absolute;display:flex;align-items:center;gap:10px}
  .brand__mark{width:22px;height:22px;background:var(--navy)}
  .brand__name{font-family:"PT Sans",sans-serif;font-weight:700;font-size:36px;line-height:1;color:var(--navy)}

  .service{position:absolute;width:130px;text-align:center;color:#fff;font-family:"Ubuntu",sans-serif;font-weight:700;font-size:14.5px;line-height:19px}
  .service__icon{position:absolute;width:64px;height:64px}

  .intro{position:absolute;color:#fff;font-size:13px;line-height:19px;text-align:justify}

  .feature__badge{position:absolute;width:66px;height:66px;border-radius:50%;background:var(--navy);border:2px solid #2a6fd0;display:flex;align-items:center;justify-content:center}
  .feature__title{position:absolute;width:210px;text-align:center;font-family:"Gelasio",serif;font-weight:700;font-size:19.5px;white-space:nowrap}
  .feature__title--blue{color:var(--link-blue)}
  .feature__text{position:absolute;font-size:13px;line-height:14.6px;text-align:justify;color:#222}

  .contact{position:absolute;color:#fff;font-size:13px;line-height:14.5px}
  .contact--phone{font-size:14.5px}

  .pricing-title{position:absolute;font-family:"Gelasio",serif;font-weight:700;font-size:54px;color:#fff;white-space:nowrap;line-height:1}
  .tier{position:absolute;left:12px;width:295px;background:var(--navy);border-left:3px solid #3c73c4}
  .tier__label{position:absolute;left:8px;top:16px;height:24px;padding:0 6px;background:#fff;font-family:"Gelasio",serif;font-weight:700;font-size:19px;line-height:24px;color:var(--ink)}
  .tier__label--gold{background:var(--gold-grey);color:#fff}
  .tier__ribbon{position:absolute;right:-1px;top:-1px;width:0;height:0;border-top:14px solid var(--ribbon);border-left:14px solid transparent}
  .tier__rows{position:absolute;left:6px;right:4px;top:47px;list-style:none}
  .tier__row{display:flex;justify-content:space-between;height:21px;line-height:20px;border-bottom:1px solid rgba(255,255,255,.35);font-family:"Gelasio",serif;font-weight:700;font-size:13.5px;color:#fff;white-space:nowrap}
  .tier__row:last-child{border-bottom:none}
  .tier__row span:last-child{width:76px}
  .note{position:absolute;left:319px;width:288px;color:var(--navy);font-size:12.6px;line-height:17px;text-align:justify}
  .note--serif{font-family:"Gelasio",serif;font-size:12.4px}
  .coupon-btn{position:absolute;left:14px;top:877px;width:137px;height:45px;border-radius:23px;background:#fff;color:var(--navy);font-family:"PT Sans",sans-serif;font-weight:700;font-size:17px;display:flex;align-items:center;justify-content:center}
  .coupon-text{position:absolute;color:#fff;white-space:nowrap}
</style>
</head>
<body>
<main class="canvas">

  <!-- Side 1: services -->
  <section class="flyer flyer--services" aria-label="Flyer side one, services">
    <svg class="flyer__shapes" viewBox="0 0 664 939" aria-hidden="true">
      <rect x="0" y="0" width="454" height="80" fill="var(--cyan)"/>
      <rect x="0" y="80" width="557" height="144" fill="var(--navy)"/>
      <polygon points="440,224 557,224 440,305" fill="var(--navy)"/>
      <rect x="0" y="200" width="40" height="739" fill="var(--cyan)"/>
      <path d="M0,224 H450 V292 Q450,319 423,319 H0 Z" fill="var(--cyan)"/>
      <path d="M30,939 V392 Q30,322 100,322 H420 Q446,322 456,296 L468,300 Q458,336 428,336 H108 Q44,336 44,400 V939 Z" fill="var(--brown)"/>
      <path d="M230,939 V870 Q230,850 250,850 H664 V939 Z" fill="var(--brown)"/>
      <path d="M242,939 V878 Q242,862 258,862 H664 V939 Z" fill="var(--cyan)"/>
      <rect x="87" y="862" width="577" height="67" fill="var(--navy)"/>
      <rect x="87" y="862" width="5" height="67" fill="#fff"/>
    </svg>

    <div class="slogan abs" style="left:31px;top:10px">One Stop&nbsp; Finance Department</div>
    <div class="slogan abs" style="left:117px;top:44px">Service for Small Businesses</div>

    <div class="brand" style="left:500px;top:22px">
      <span class="brand__mark"></span><span class="brand__name">TQB</span>
    </div>

    <svg class="service__icon" style="left:48px;top:90px" viewBox="0 0 64 64" aria-hidden="true">
      <rect x="12" y="22" width="40" height="30" rx="4" fill="#fff"/>
      <rect x="18" y="12" width="26" height="12" rx="2" fill="#fff" transform="rotate(-12 31 18)"/>
      <rect x="40" y="31" width="14" height="10" rx="3" fill="var(--navy)"/>
      <circle cx="46" cy="36" r="2.5" fill="#fff"/>
    </svg>
    <div class="service" style="left:15px;top:172px">Bookkeeping &amp;<br>Payroll</div>

    <svg class="service__icon" style="left:175px;top:90px" viewBox="0 0 64 64" aria-hidden="true">
      <rect x="14" y="8" width="36" height="48" rx="4" fill="none" stroke="#fff" stroke-width="4"/>
      <rect x="21" y="18" width="22" height="4" fill="#fff"/>
      <rect x="21" y="28" width="12" height="3" fill="#fff"/>
      <rect x="21" y="36" width="12" height="3" fill="#fff"/>
      <rect x="21" y="44" width="12" height="3" fill="#fff"/>
      <text x="41" y="46" font-family="PT Sans,sans-serif" font-weight="700" font-size="16" fill="#fff" text-anchor="middle">$</text>
    </svg>
    <div class="service" style="left:137px;top:172px">Taxation<br>Compliance</div>

    <svg class="service__icon" style="left:297px;top:90px" viewBox="0 0 64 64" aria-hidden="true">
      <g stroke="#fff" stroke-width="3"><line x1="32" y1="36" x2="10" y2="40"/><line x1="32" y1="36" x2="54" y2="40"/><line x1="32" y1="36" x2="20" y2="56"/><line x1="32" y1="36" x2="44" y2="56"/></g>
      <circle cx="32" cy="12" r="7" fill="#fff"/>
      <path d="M18,34 Q18,21 32,21 Q46,21 46,34 Z" fill="#fff"/>
      <circle cx="10" cy="40" r="5" fill="#fff"/><circle cx="54" cy="40" r="5" fill="#fff"/>
      <circle cx="20" cy="56" r="5" fill="#fff"/><circle cx="44" cy="56" r="5" fill="#fff"/>
    </svg>
    <div class="service" style="left:261px;top:172px">Management<br>Accounting</div>

    <svg class="service__icon" style="left:424px;top:90px" viewBox="0 0 64 64" aria-hidden="true">
      <circle cx="38" cy="18" r="8" fill="#fff"/>
      <circle cx="50" cy="8" r="5" fill="none" stroke="#fff" stroke-width="2"/>
      <path d="M4,42 Q14,32 26,36 L40,36 Q46,38 40,42 L28,42 L44,44 L58,34 Q62,36 58,40 L44,52 Q38,56 30,54 L12,50 Z" fill="#fff"/>
    </svg>
    <div class="service" style="left:392px;top:172px;width:150px">Commercial<br>Finance &amp; Mortgage</div>

    <p class="intro" style="left:26px;top:243px;width:392px">We are dedicated to share small business owner's administration burden, free business owners to focus on more value adding areas. We work as independent contrators for your business needs.</p>

    <!-- Why us, row one -->
    <div class="feature__badge" style="left:100px;top:359px">
      <svg width="36" height="36" viewBox="0 0 36 36" aria-hidden="true"><rect x="3" y="10" width="30" height="21" rx="3" fill="#fff"/><rect x="12" y="5" width="12" height="7" rx="2" fill="none" stroke="#fff" stroke-width="2.5"/><rect x="11" y="12" width="2" height="19" fill="var(--navy)"/><rect x="23" y="12" width="2" height="19" fill="var(--navy)"/></svg>
    </div>
    <div class="feature__title feature__title--blue" style="left:50px;top:438px">We work for you</div>
    <p class="feature__text" style="left:74px;top:479px;width:169px">We work like employees for your business, take responsibilities like employee does. You enjoy hassle free for your PAYG withholding, Superannuation Guarantee obligations, and leave entitlements.</p>

    <div class="feature__badge" style="left:314px;top:357px">
      <svg width="36" height="40" viewBox="0 0 36 40" aria-hidden="true"><polygon points="14,2 22,2 20,8 16,8" fill="#fff"/><polygon points="16,9 20,9 24,30 18,38 12,30" fill="#fff"/></svg>
    </div>
    <div class="feature__title" style="left:248px;top:438px">Corporate Standard</div>
    <p class="feature__text" style="left:260px;top:479px;width:186px">We hire qualified professionals and invest heavily on training, along with our testified 'Preparation + Checklist + Review' structure, we meet industry aspiration at the best of our knowledge.</p>

    <div class="feature__badge" style="left:521px;top:359px">
      <svg width="38" height="38" viewBox="0 0 38 38" aria-hidden="true"><circle cx="14" cy="15" r="8" fill="none" stroke="#fff" stroke-width="5" stroke-dasharray="4 2.3"/><circle cx="14" cy="15" r="3" fill="#fff"/><circle cx="27" cy="27" r="6" fill="none" stroke="#fff" stroke-width="4" stroke-dasharray="3 2"/></svg>
    </div>
    <div class="feature__title feature__title--blue" style="left:457px;top:438px">Utilize Technology</div>
    <p class="feature__text" style="left:462px;top:479px;width:178px">We work with our clients as a team, we use technology to improve information sharing so that clients and us on the same page, and improve efficiency and productivity by following.</p>

    <!-- Why us, row two -->
    <div class="feature__badge" style="left:102px;top:591px">
      <svg width="34" height="34" viewBox="0 0 34 34" aria-hidden="true"><path d="M3,3 H26 L31,8 V31 H3 Z" fill="#fff"/><rect x="9" y="3" width="14" height="9" fill="var(--navy)"/><rect x="8" y="17" width="18" height="12" fill="var(--navy)"/><g fill="#fff"><rect x="10" y="20" width="14" height="1.6"/><rect x="10" y="23" width="14" height="1.6"/><rect x="10" y="26" width="14" height="1.6"/></g></svg>
    </div>
    <div class="feature__title" style="left:39px;top:675px">Solid Data</div>
    <p class="feature__text" style="left:73px;top:716px;width:170px">In the meantime of keeping your accounts, we will be maintaining your database from sales, purchases suppliers, customers, employees, and other stakeholders, which are helpful for decision making.</p>

    <div class="feature__badge" style="left:305px;top:589px">
      <svg width="44" height="44" viewBox="0 0 44 44" aria-hidden="true"><circle cx="22" cy="22" r="18" fill="none" stroke="#fff" stroke-width="3"/><polygon points="34,30 42,28 38,36" fill="#fff"/><rect x="12" y="13" width="20" height="13" rx="1" fill="none" stroke="#fff" stroke-width="2.5"/><rect x="18" y="28" width="8" height="2.5" fill="#fff"/></svg>
    </div>
    <div class="feature__title feature__title--blue" style="left:244px;top:675px">Monitor Complaince</div>
    <p class="feature__text" style="left:261px;top:718px;width:182px">As we work as employee for your business, we take the responsibility to monitor and remind you for tax compliance requirement, and work together with you to fulfil the requirement.</p>

    <div class="feature__badge" style="left:525px;top:589px">
      <svg width="34" height="34" viewBox="0 0 34 34" aria-hidden="true"><circle cx="17" cy="10" r="7" fill="#fff"/><path d="M4,31 Q4,19 17,19 Q30,19 30,31 Z" fill="#fff"/></svg>
    </div>
    <div class="feature__title feature__title--blue" style="left:457px;top:675px">Finance Analyst</div>
    <p class="feature__text" style="left:462px;top:718px;width:178px">With your consent, we will be dealing with NRB, financial institutions and other finance related stakeholders on your behalf for better efficiency and effectiveness, as we speak their business language.</p>

    <!-- Contact -->
    <svg class="abs" style="left:106px;top:872px" width="28" height="26" viewBox="0 0 28 26" aria-hidden="true"><polygon points="14,1 27,13 23,13 23,25 17,25 17,17 11,17 11,25 5,25 5,13 1,13" fill="#fff"/></svg>
    <p class="contact" style="left:145px;top:875px">Address: 58 Dunmore Street,&nbsp; Brindale, WA 6107<br>PO Box 2493, West Harlow,<br>WA 6983</p>
    <p class="contact" style="left:459px;top:874px">hello@tqbfsx.com.au</p>
    <svg class="abs" style="left:435px;top:893px" width="18" height="24" viewBox="0 0 18 24" aria-hidden="true"><path d="M4,1 L8,1 L9,7 L6,9 Q8,15 12,18 L15,15 L18,19 L16,23 Q10,24 5,17 Q0,10 1,4 Z" fill="#fff"/></svg>
    <p class="contact contact--phone" style="left:458px;top:894px">(08) 6287 3914&nbsp; / 0491 738 226</p>
  </section>

  <!-- Side 2: pricing -->
  <section class="flyer flyer--pricing" aria-label="Flyer side two, pricing">
    <svg class="flyer__shapes" viewBox="0 0 664 939" aria-hidden="true">
      <rect x="200" y="0" width="464" height="78" fill="var(--cyan)"/>
      <rect x="92" y="78" width="572" height="144" fill="var(--navy)"/>
      <polygon points="92,222 210,222 210,252" fill="var(--navy)"/>
      <rect x="622" y="250" width="42" height="689" fill="var(--cyan)"/>
      <path d="M204,222 H664 V312 H244 Q204,312 204,272 Z" fill="var(--cyan)"/>
      <path d="M262,312 H566 Q638,312 638,384 V939 H624 V390 Q624,326 562,326 H286 Q266,326 262,312 Z" fill="var(--brown)"/>
      <path d="M0,858 H424 Q442,858 444,876 V939 H0 Z" fill="var(--brown)"/>
      <path d="M0,866 H420 Q434,866 436,880 V939 H0 Z" fill="var(--cyan)"/>
      <rect x="0" y="870" width="584" height="60" fill="var(--navy)"/>
      <rect x="584" y="870" width="80" height="60" fill="var(--cyan)"/>
      <rect x="579" y="870" width="5" height="60" fill="#fff"/>
    </svg>

    <div class="brand" style="left:22px;top:20px">
      <span class="brand__mark"></span><span class="brand__name">TQB</span>
    </div>
    <div class="slogan abs" style="left:243px;top:9px">One Stop&nbsp; Finance Department</div>
    <div class="slogan abs" style="left:329px;top:42px">Service for Small Businesses</div>

    <svg class="abs" style="left:200px;top:105px" width="84" height="84" viewBox="0 0 84 84" aria-hidden="true">
      <circle cx="42" cy="42" r="42" fill="#fff"/>
      <path d="M28,20 H52 L60,30 V62 Q60,66 56,66 H28 Q24,66 24,62 V24 Q24,20 28,20 Z" fill="var(--navy)" transform="rotate(-25 42 42)"/>
      <circle cx="48" cy="24" r="3.5" fill="#fff" transform="rotate(-25 42 42)"/>
      <text x="43" y="56" font-family="PT Sans,sans-serif" font-weight="700" font-size="30" fill="#fff" text-anchor="middle" transform="rotate(-25 42 46)">$</text>
    </svg>
    <h1 class="pricing-title" style="left:313px;top:118px">Our Pricing</h1>

    <p class="intro" style="left:268px;top:248px;width:384px;text-align:left">As we are an independent contractor look after your business, save cost is always in our sight, even for your finance department cost.</p>

    <div class="tier" style="top:355px;height:159px">
      <div class="tier__label">Bronze</div>
      <ul class="tier__rows">
        <li class="tier__row"><span>Bookkeeping &amp; Payroll:</span><span>$50/hr</span></li>
        <li class="tier__row"><span>Taxation:</span><span>$110/hr</span></li>
        <li class="tier__row"><span>Management Accounting:</span><span>$110/hr</span></li>
        <li class="tier__row"><span>Finance:</span><span>POA, Free</span></li>
        <li class="tier__row"><span>General Consulting:</span><span>Free*</span></li>
      </ul>
    </div>
    <p class="note note--serif" style="top:378px">Rate above applies for using us for bookkeeping or payroll or taxation or management accounting service only.</p>
    <p class="note note--serif" style="top:446px">Other fees/charges may apply for client subscriptions, e.g. accounting software subscription, currently around $50/month.</p>

    <div class="tier" style="top:525px;height:160px">
      <div class="tier__label tier__label--gold">Gold<span class="tier__ribbon"></span></div>
      <ul class="tier__rows">
        <li class="tier__row"><span>Bookkeeping &amp; Payroll:</span><span>$45/hr</span></li>
        <li class="tier__row"><span>Taxation:</span><span>$99/hr</span></li>
        <li class="tier__row"><span>Management Accounting:</span><span>$99/hr</span></li>
        <li class="tier__row"><span>Finance:</span><span>POA, Free</span></li>
        <li class="tier__row"><span>General Consulting:</span><span>Free*</span></li>
      </ul>
    </div>
    <p class="note" style="top:554px">Rate above applies for using us for bookkeeping or payroll or management accounting and taxation services.</p>
    <p class="note" style="top:604px">Other fees/charges may apply for client subscriptions, e.g. accounting software subscription, currently around $50/month.</p>

    <div class="tier" style="top:692px;height:155px">
      <div class="tier__label">Platinum</div>
      <ul class="tier__rows">
        <li class="tier__row"><span>Bookkeeping &amp; Payroll:</span><span>$40/hr</span></li>
        <li class="tier__row"><span>Taxation:</span><span>$88/hr</span></li>
        <li class="tier__row"><span>Management Accounting:</span><span>$88/hr</span></li>
        <li class="tier__row"><span>Finance:</span><span>POA, Free</span></li>
        <li class="tier__row"><span>General Consulting:</span><span>Free*</span></li>
      </ul>
    </div>
    <p class="note" style="top:719px">Rate above applies for using us for bookkeeping or payroll and taxation and management accounting services.</p>
    <p class="note" style="top:769px">Other fees/charges may apply for client subscriptions, e.g. accounting software subscription, currently around $50/month.</p>

    <div class="coupon-btn">Sign Up Now!</div>
    <p class="coupon-text" style="left:261px;top:877px;font-size:15px">receive 10% off for your next 12 months bil</p>
    <p class="coupon-text" style="right:92px;top:898px;font-size:20px;font-weight:700">Valid until 31/07/2016</p>
  </section>

</main>
</body>
</html>
```